Flyer-Design für Gefäßchirurg
Zielgruppe
Niedergelassener Gefäßchirurg in eigener (Einzel-) Praxis; zZt 4 Angestellte (1 Krankenschwester, eine MFA, eine Azubi, eine Reinigungskraft); tätig in der Stadt Plön (24306); im Kreis Plön nur ein weiter ALLGEMEIN chirurg; HP: www.praxisdoktor-haverbeck.de ; Kernkompetenz: Diagnostik und Therapie von Gefäßerkrankungen (z.B. Krampfadern, Durchblutungsstörungen... (s.auch HP); eigener OP in der Praxis; hier Versorgung u.a. von Krampfadern aber auch andere chirurgische Eingriffe;
Aufgabenstellung
Bzgl. des Formates keine Festlegung bevorzuge aber Format Din lang hoch oder Din a 5 hoch ; Flyer soll übersichtlich Behandlungen der Praxis benennen; insbesondere um auch außerhalb der Gefäßchirurgie weitere chirurgische Patienten zu gewinnen (z.B. chirurgische Entfernung kleiner Pigmentflecke, eingewachsener Nagel, aber auch 'Wegspritzen/ Sklerosierung' von Besenreisern, eingewachsener Zehennagel), ggf. mit Anfahrtskarte, Parkplätze vor der Tür; falls nicht zu Kostenintensiv: auch Nutzung von Stock - Bildern (ca. Obergrenze für Bildmaterial 50,- €);
mir ist bewusst, dass die Photos der Angestellten und mir nicht 100% scharf sind; falls diese verwendet werden, könnten diese z.B. kleinformatig auf dem flyer erscheinen, oder ich würde diese im Verlauf noch einmal aufnehmen. Ob und wieviele der Photos auf dem flyer sind, überlasse ich Ihnen.

```html
<!DOCTYPE html>
<html lang="de">
<head>
<meta charset="utf-8">
<title>Flyer Gefäßmedizin / Chirurgie</title>
<link href="https://fonts.googleapis.com/css2?family=Tenor+Sans&family=Encode+Sans+Semi+Condensed:wght@400;600&display=swap" rel="stylesheet">
<style>
  :root {
    --paper: #efebea;
    --gutter: #ffffff;
    --red-deep: #8e0a10;
    --red: #d3202a;
    --red-light: #ef5b5b;
    --ink: #3a3a3a;
    --ink-soft: #4a4a4a;
    --white: #ffffff;
  }
  * { box-sizing: border-box; margin: 0; padding: 0; }
  html, body { width: 1200px; height: 839px; overflow: hidden; background: var(--gutter); }
  body { position: relative; font-family: "Encode Sans Semi Condensed", Arial, sans-serif; color: var(--ink); }

  .page { position: absolute; top: 0; height: 839px; background: var(--paper); overflow: hidden; }
  .page--front { left: 0; width: 597px; }
  .page--services { left: 605px; width: 595px; }

  .hero-band {
    position: absolute; left: 0; top: 0; width: 100%;
    background:
      radial-gradient(ellipse 160px 90px at 30% 70%, var(--red-light), transparent 70%),
      radial-gradient(ellipse 200px 120px at 80% 30%, var(--red-light), transparent 70%),
      radial-gradient(ellipse 140px 80px at 60% 90%, var(--red-deep), transparent 70%),
      linear-gradient(135deg, var(--red-deep), var(--red) 45%, #b3141c);
  }
  .page--front .hero-band { height: 298px; }
  .page--services .hero-band { height: 232px; }

  .hero-title {
    position: absolute; top: 22px; left: 30px;
    font-family: "Tenor Sans", Arial, sans-serif; font-weight: 400;
    font-size: 55px; line-height: 53px; color: var(--white); letter-spacing: -0.5px;
  }

  .photo { position: absolute; border: 2px solid var(--white); }
  .photo--doctor { left: 374px; top: 152px; width: 185px; height: 229px; background: linear-gradient(180deg, #e8e8e8 0%, #c9bfb8 50%, #1d2635 100%); }
  .photo--team { left: 31px; width: 72px; height: 89px; border: none; background: linear-gradient(180deg, #d8d6d4 0%, #b49a8c 55%, #2a2c38 100%); }

  .practice-mark { position: absolute; left: 196px; top: 352px; }
  .practice-mark__name { font-family: "Tenor Sans", Arial, sans-serif; font-size: 15.5px; color: var(--ink-soft); display: flex; align-items: center; gap: 6px; }
  .practice-mark__square { width: 9px; height: 9px; background: var(--red); display: inline-block; }
  .practice-mark__sub { font-size: 7.5px; color: var(--ink-soft); }
  .career-note { position: absolute; left: 197px; top: 386px; font-size: 11px; color: var(--ink-soft); }

  .team-heading { position: absolute; left: 33px; top: 439px; font-size: 15px; font-weight: 600; color: var(--ink); }
  .team-caption { position: absolute; left: 31px; font-size: 9.4px; line-height: 11.5px; color: var(--ink-soft); }

  .welcome { position: absolute; left: 195px; top: 425px; width: 362px; }
  .welcome__title { font-size: 19.5px; font-weight: 600; color: var(--ink); margin-bottom: 8px; letter-spacing: -0.2px; }
  .welcome p { font-size: 10.3px; line-height: 13.5px; text-align: justify; hyphens: auto; margin-bottom: 3px; color: var(--ink-soft); }
  .welcome strong { font-weight: 600; color: var(--ink); }

  .conditions { position: absolute; left: 195px; top: 596px; width: 362px; font-size: 10.5px; line-height: 13.3px; color: var(--ink-soft); }
  .conditions__title { text-align: center; font-weight: 600; color: var(--ink); padding-left: 14px; }
  .conditions__cols { display: flex; }
  .conditions__col--left { width: 176px; text-align: right; }
  .conditions__col--right { padding-left: 10px; }

  .map-area { position: absolute; left: 196px; top: 705px; width: 150px; height: 100px; background: linear-gradient(135deg, #f4f4f4 0%, #e3e3e3 60%, #b9dcf0 100%); }
  .parking-note { position: absolute; left: 196px; top: 808px; font-size: 10.3px; color: var(--ink-soft); }

  .address { position: absolute; right: 59px; top: 702px; text-align: right; font-size: 10.3px; line-height: 13.6px; color: var(--ink-soft); font-style: normal; }
  .address__street { margin-top: 3px; }
  .contact { position: absolute; right: 39px; top: 769px; font-size: 10.3px; line-height: 13.4px; color: var(--ink-soft); }
  .contact__row { display: flex; justify-content: flex-end; align-items: center; gap: 7px; }
  .contact__row svg { width: 11px; height: 11px; }

  .service-photos { position: absolute; left: 18px; top: 175px; display: flex; gap: 7px; }
  .service-photo { width: 106px; height: 106px; border: 2px solid var(--white); }
  .service-photo--skin { background: linear-gradient(160deg, #c99a80, #7d5546); }
  .service-photo--surgery { background: linear-gradient(160deg, #dfe6ef, #3a5bc4); }
  .service-photo--ultrasound { background: linear-gradient(160deg, #e6e6e6, #c7b5a6); }
  .service-photo--gloves { background: linear-gradient(160deg, #3c8fd9, #d4a98e); }
  .service-photo--toe { background: linear-gradient(160deg, #f3f3f3, #d8a899); }

  .service-list { position: absolute; left: 63px; top: 303px; width: 462px; }
  .service { margin-bottom: 7px; }
  .service__title { font-size: 17.5px; font-weight: 600; color: var(--ink); line-height: 22px; letter-spacing: -0.2px; }
  .service__text { font-size: 11.5px; line-height: 16px; color: var(--ink-soft); }

  .appointment-note { position: absolute; left: 63px; top: 774px; width: 470px; font-size: 8.8px; line-height: 11.5px; color: var(--ink-soft); }
  .appointment-note strong { font-weight: 600; color: var(--ink); }
  .insurance-note { position: absolute; left: 0; width: 100%; top: 808px; text-align: center; font-size: 11.3px; color: var(--ink-soft); padding-left: 36px; }
</style>
</head>
<body>

<section class="page page--front">
  <div class="hero-band" role="img" aria-label="Nahaufnahme roter Blutkörperchen in einem Blutgefäß"></div>
  <h1 class="hero-title">Gefäßmedizin/<br>Chirurgie</h1>

  <div class="photo photo--doctor" role="img" aria-label="Porträtfoto des Praxisinhabers"></div>

  <div class="practice-mark">
    <div class="practice-mark__name">Dr. Jonas Haverbeck <span class="practice-mark__square"></span></div>
    <div class="practice-mark__sub">Praxis für Gefäßmedizin und Chirurgie</div>
  </div>
  <div class="career-note">ehemals leitender Oberarzt in der Klinik für Gefäßmedizin in Friedrichsau</div>

  <h2 class="team-heading">Mein Team</h2>
  <div class="photo photo--team" style="top:462px" role="img" aria-label="Porträtfoto der Auszubildenden"></div>
  <div class="team-caption" style="top:551px">Lena Kowalczyk<br>AZUBI</div>
  <div class="photo photo--team" style="top:581px" role="img" aria-label="Porträtfoto der Krankenschwester"></div>
  <div class="team-caption" style="top:670px">Svenja Reimers<br>Krankenschwester</div>
  <div class="photo photo--team" style="top:702px" role="img" aria-label="Porträtfoto der Medizinischen Fachangestellten am Telefon"></div>
  <div class="team-caption" style="top:791px">Anke Petersen<br>MFA</div>

  <div class="welcome">
    <h2 class="welcome__title">Ich begrüße Sie herzlich in unserer Praxis!</h2>
    <p>Gerne kümmern wir uns um Ihre gefäßmedizinischen und chirurgischen Anliegen.</p>
    <p>Als <strong>Gefäßchirurg</strong> und <strong>Phlebologe</strong> besitze ich eine besondere Erfahrung in der Therapie und Diagnostik von <strong>gefäßmedizinischen Erkrankungen</strong>.</p>
    <p>Mit einem hochwertigen <strong>Ultraschallgerät</strong> sowie durch einen in die Praxis integrierten <strong>Operationsraum</strong> und einem Aufwachraum sind optimale Bedingungen gegeben. Bezüglich der operativen Versorgung des Krampfaderleidens halten wir alle gängigen Operationsmethoden vor.</p>
    <p>Abseits der gefäßmedizinischen Erkrankungen sind wir auch für <strong>kleinere chirurgischen Maßnahmen</strong> Ihr Ansprechpartner.</p>
  </div>

  <div class="conditions">
    <div class="conditions__title">Krankheitsbilder</div>
    <div class="conditions__cols">
      <div class="conditions__col--left">Krampfadern<br>Besenreiser<br>Schaufensterkrankheit<br>Bauchaortenaneurysma<br>Bewertung des Schlaganfallrisikos</div>
      <div class="conditions__col--right">Durchblutungsstörung<br>Pigmentflecken<br>Hauttumoren<br>Nagelbettentzündung<br>Entfernung kleiner Pigmentflecke</div>
    </div>
  </div>

  <div class="map-area" role="img" aria-label="Anfahrtskarte zur Praxis mit See und Straßen"></div>
  <div class="parking-note">Parkplätze vor der Tür</div>

  <address class="address">
    Dr. Jonas Haverbeck<br>Praxis für Gefäßmedizin,<br>Gefäßchirurgie und Phlebologie
    <div class="address__street">Lindenweg 12 - 23999 Holmbek</div>
  </address>

  <div class="contact">
    <div class="contact__row">04599 3158 420
      <svg viewBox="0 0 24 24"><path d="M6.6 10.8a15 15 0 0 0 6.6 6.6l2.2-2.2c.3-.3.7-.4 1-.2 1.1.4 2.3.6 3.6.6.6 0 1 .4 1 1V20c0 .6-.4 1-1 1A17 17 0 0 1 3 4c0-.6.4-1 1-1h3.5c.6 0 1 .4 1 1 0 1.3.2 2.5.6 3.6.1.3 0 .7-.2 1z" fill="#333"/></svg>
    </div>
    <div class="contact__row">04599 3158 429
      <svg viewBox="0 0 24 24" fill="none" stroke="#333" stroke-width="2"><rect x="6" y="3" width="12" height="6"/><rect x="3" y="9" width="18" height="9"/><rect x="7" y="14" width="10" height="7" fill="#fff"/></svg>
    </div>
    <div class="contact__row">info@praxisdoktor-haverbeck.de
      <svg viewBox="0 0 24 24" fill="none" stroke="#333" stroke-width="2"><rect x="3" y="5" width="18" height="14"/><path d="M3 5l9 8 9-8"/></svg>
    </div>
    <div class="contact__row">www.praxisdoktor-haverbeck.de
      <svg viewBox="0 0 24 24" fill="none" stroke="#333" stroke-width="2"><circle cx="12" cy="12" r="9"/><ellipse cx="12" cy="12" rx="4" ry="9"/><path d="M3 12h18"/></svg>
    </div>
  </div>
</section>

<section class="page page--services">
  <div class="hero-band" role="img" aria-label="Nahaufnahme roter Blutkörperchen in einem Blutgefäß"></div>
  <h1 class="hero-title">Krankheitsbilder/<br>Leistungen</h1>

  <div class="service-photos">
    <div class="service-photo service-photo--skin" role="img" aria-label="Foto: Bein mit Krampfadern"></div>
    <div class="service-photo service-photo--surgery" role="img" aria-label="Foto: kleiner chirurgischer Eingriff mit Skalpell"></div>
    <div class="service-photo service-photo--ultrasound" role="img" aria-label="Foto: Ultraschalluntersuchung am Bein"></div>
    <div class="service-photo service-photo--gloves" role="img" aria-label="Foto: Sklerosierung von Besenreisern"></div>
    <div class="service-photo service-photo--toe" role="img" aria-label="Foto: Zehe mit Nagelbettentzündung"></div>
  </div>

  <div class="service-list">
    <div class="service"><h3 class="service__title">Krampfadern</h3><p class="service__text">Lorem ipsum dolor sit amet, consetetur sadipscing elitr, sed diam nonumy eirmod tempor</p></div>
    <div class="service"><h3 class="service__title">Besenreiser</h3><p class="service__text">Lorem ipsum dolor sit amet, consetetur sadipscing elitr, sed diam nonumy</p></div>
    <div class="service"><h3 class="service__title">Schaufensterkrankheit</h3><p class="service__text">Lorem ipsum dolor sit amet, consetetur sadipscing elitr, sed diam nonumy eirmod tempor<br>invidunt ut labore et dolore magna</p></div>
    <div class="service"><h3 class="service__title">Bauchaortenaneurysma</h3><p class="service__text">Lorem ipsum dolor sit amet, consetetur sadipscing elitr, sed diam nonumy</p></div>
    <div class="service"><h3 class="service__title">Bewertung des Schlaganfallrisikos</h3><p class="service__text">Lorem ipsum dolor sit amet, consetetur sadipscing elitr, sed diam nonumy eirmod tempor<br>invidunt ut labore et dolore magna</p></div>
    <div class="service"><h3 class="service__title">Durchblutungsstörung der Hände und Füße</h3><p class="service__text">Lorem ipsum dolor sit amet, consetetur sadipscing elitr, sed diam nonumy</p></div>
    <div class="service"><h3 class="service__title">Pigmentflecken oder kleine Hauttumoren</h3><p class="service__text">Lorem ipsum dolor sit amet, consetetur sadipscing elitr, sed diam nonumy eirmod tempor</p></div>
    <div class="service"><h3 class="service__title">Nagelbettentzündung</h3><p class="service__text">Lorem ipsum dolor sit amet, consetetur sadipscing elitr, sed diam nonumy</p></div>
    <div class="service"><h3 class="service__title">Entfernung kleiner Pigmentflecke</h3><p class="service__text">Lorem ipsum dolor sit amet, consetetur sadipscing elitr, sed diam nonumy eirmod tempor<br>invidunt ut labore et dolore magna</p></div>
  </div>

  <p class="appointment-note">Wir bieten unseren Patienten eine <strong>Terminsprechstunde</strong> an. Dies hat den Vorteil, dass Wartezeiten auf ein Minimum beschränkt werden. Gerne vergeben wir Ihnen unter 04599 3158420 einen für Sie passenden Termin.</p>
  <p class="insurance-note">Die gesetzlichen Krankenkassen übernehmen in großen Teilen die aufgeführte Diagnostik und Therapie.</p>
</section>

</body>
</html>
```